Background on the company
=======================
This is a Bitcoin Consulting Company.

We have two projects.

Tinted Tokens: software to trade assets over the Bitcoin protocol (assets like property, traditional currencies, gold, stocks, securities, bonds, etc.).

Vaultrix Home Teller: a hardware based web service in a box that manages cold storage wallets and off line transaction signing. It is the secure way to deploy a web wallet without relying on third parties.

All that to say this is a high tech company focusing on Bitcoin.

What does Drellowmar mean?
========================

The Beast of Drellowmar is the rabbit in Quimby Larkets's Silver Goblet that defeats his band of knights. (At least until they go and get the Holy Hand Grenade).

We like this, because we are a deceptively soft and fuzzy company that is also killer!

What We Need:
============

Primarily we need to get the logo designed. I have a hand drawing I did, but you are not limited to that. And the logo needs to work on a business card. The right logo that works on a Business Card is the primary consideration.
Updates

The main task here is to get the logo right.  I have provided a drawing I made, and I like it, but my complaints are:  Drellowmar is hard to read.  The 'C' isn't obvious.

We can fix this many ways.  We can forget the whole "combinde a rabit with the C and a" idea.  We can add "Drellowmar Systems" on the card apart from the logo (that way if they don't "get it" they can still read it.)

The Rabbit itself is quite obviously scanned from a hand drawing.  That might not be a bad thing, but combine that with the entire logo, and it is too cheap looking.

Target Market(s)

Technical folks. Investors. Business contacts.

Industry/Entity Type

Software

Requirements
Must have
• We have to clean up the logo, or replace it with something that hints at the same sort of things. (See the upload) Basically and innocent white bunny. Something that works on a Business Card.

All the information below:

Derek Hale
ph (555) 314-9072
hale.derek@mailvora.net
derek@drellowmar.net
Nice to have
• I would like it to be serious, yet whimsical. An inside joke, so you get it if you know Quimby Larkets. But otherwise, it looks reasonably serious if you don't know Quimby Larkets.

I don't want it to be scary. (oddly, that my own efforts seem to make that easy to do)

Would like a set of colors that remind one of a cave, a rabbit, knights.... Not sure what those are...

```html
<!DOCTYPE html>
<html lang="en">
<head>
<meta charset="utf-8">
<title>Drellowmar Systems — Business Card</title>
<link rel="stylesheet" href="https://fonts.googleapis.com/css2?family=Open+Sans:wght@400;700&display=swap">
<style>
  :root {
    --stage: #b4b4b6;
    --card-dark: #3d3d3f;
    --card-light: #ffffff;
    --brand-green: #7dc242;
    --text-light: #ffffff;
    --text-dark: #3d3d3f;
  }
  * { box-sizing: border-box; margin: 0; padding: 0; }
  html, body {
    width: 1200px;
    height: 900px;
    overflow: hidden;
  }
  body {
    position: relative;
    background: var(--stage);
    font-family: "Open Sans", Arial, sans-serif;
  }
  .card {
    position: absolute;
    width: 600px;
    height: 340px;
    overflow: hidden;
    box-shadow: 0 10px 30px rgba(0, 0, 0, 0.25);
  }

  /* Back of card */
  .card-back {
    left: 110px;
    top: 90px;
    background: var(--card-dark);
    display: flex;
    align-items: center;
    justify-content: center;
  }
  .brand-name {
    font-weight: 700;
    line-height: 1.05;
  }
  .card-back .brand-name {
    color: var(--text-light);
    font-size: 46px;
    text-align: left;
  }
  .brand-name .brand-line { display: block; }

  /* Front of card */
  .card-front {
    left: 490px;
    top: 470px;
    background: var(--card-light);
  }
  .card-front .brand-name {
    position: absolute;
    left: 40px;
    top: 70px;
    color: var(--brand-green);
    font-size: 44px;
  }
  .contact-block {
    position: absolute;
    right: 0;
    top: 120px;
    width: 290px;
    height: 220px;
    background: var(--card-dark);
    border-top-left-radius: 60px;
    padding: 34px 0 0 44px;
  }
  .contact-name {
    color: var(--brand-green);
    font-weight: 700;
    font-size: 19px;
    letter-spacing: 0.5px;
    margin-bottom: 14px;
  }
  .contact-list { list-style: none; }
  .contact-item {
    display: flex;
    align-items: center;
    gap: 10px;
    color: var(--text-light);
    font-size: 14px;
    margin-bottom: 7px;
  }
  .contact-icon {
    width: 14px;
    height: 14px;
    flex: none;
  }
</style>
</head>
<body>

  <section class="card card-back" aria-label="Card back">
    <p class="brand-name">
      <span class="brand-line">Drellowmar</span>
      <span class="brand-line">Systems</span>
    </p>
  </section>

  <section class="card card-front" aria-label="Card front">
    <p class="brand-name">
      <span class="brand-line">Drellowmar</span>
      <span class="brand-line">Systems</span>
    </p>

    <div class="contact-block">
      <p class="contact-name">DEREK HALE</p>
      <ul class="contact-list">
        <li class="contact-item">
          <svg class="contact-icon" viewBox="0 0 14 14" aria-hidden="true">
            <rect width="14" height="14" rx="2" fill="#7dc242"/>
            <rect x="4.5" y="2.5" width="5" height="9" rx="1" fill="none" stroke="#3d3d3f" stroke-width="1.3"/>
          </svg>
          <span>(555) 314-9072</span>
        </li>
        <li class="contact-item">
          <svg class="contact-icon" viewBox="0 0 14 14" aria-hidden="true">
            <rect width="14" height="14" rx="2" fill="#7dc242"/>
            <path d="M3 4.5h8v5.5H3z M3 4.5l4 3 4-3" fill="none" stroke="#3d3d3f" stroke-width="1.2"/>
          </svg>
          <span>hale.derek@mailvora.net</span>
        </li>
        <li class="contact-item">
          <svg class="contact-icon" viewBox="0 0 14 14" aria-hidden="true">
            <rect width="14" height="14" rx="2" fill="#7dc242"/>
            <path d="M3 4.5h8v5.5H3z M3 4.5l4 3 4-3" fill="none" stroke="#3d3d3f" stroke-width="1.2"/>
          </svg>
          <span>derek@drellowmar.net</span>
        </li>
      </ul>
    </div>
  </section>

</body>
</html>
```